new service company in the field of construction seeks to make the Creation of a PPT

We need a PPT format with a cover page a frame for presentation. our company is based in Paris which was named VERNAPLO. we just did our logo attached. Our company offers services to manage and control documents that pass on projects in construction (building, infrastructure, energy, oil and gas etc. ..). We use internet systems to help us, design must show insurance, quality, and safety. Customers should build any type of works and can not build without the approved documents. These documents go through multiple validations, and vernaplo staff seconded on projects, coordinate these processes and documents, quality documents, to ensure that project deadlines are met and project management sees his project developed within the period, through regular reporting. the services offered by our company help ensure the project of building on time, to ensure the project manager visibility on what e will not, and can act accordingly.

Target Market(s)

general contractor of engineering construction or big business masters lumber wholesale real estate investor, project ownership in the construction sector

Industry/Entity Type

Construction

Contact Information for Business Card

carte rectangulaire petite taille (4X6cm env)
horizontale ou verticale
prendre en compte les éléments suivants :
logo
nom de société
adresse postale (4 lignes)
teléphone:
mail
role (ex : directeur)
in the back : La qualité documentaire de vos projets

Font styles to use
Sans Serif

Colors
34a7d7
85cae6
cee9f5
0592cd

Requirements
Must have
• The project should have 2 sliders: slider 1. Cover Page 2. slider for the content of presentations THE GOAL IS TO HAVE A VISUAL IDENTITY ON PPT, MY BUSINESS CARDS AND LETTERS must stay in mind and colors of the logo that joined the design must be clean and recall the seriousness, ease. the design must take into account the page numbers Tag line: the documentary quality of your projects information such as tagline and writes must be modifiable
Nice to have
• would require the presentation of the figure shows concepts or reporting table THE GOAL IS TO HAVE A VISUAL IDENTITY ON PPT, MY BUSINESS CARDS AND LETTERS
Should not have
• not to building or building in the logo

```html
<!DOCTYPE html>
<html lang="en">
<head>
<meta charset="utf-8">
<title>VERNAPLO presentation template</title>
<link href="https://fonts.googleapis.com/css2?family=Raleway:wght@400;500;600;700&family=Montserrat:wght@400;600;700&display=swap" rel="stylesheet">
<style>
:root{
  --blue:#2b6cb4;
  --blue-deep:#1f5ea8;
  --blue-mid:#4a86c8;
  --blue-soft:#7ea9dc;
  --blue-pale:#cfdff1;
  --ink:#4a4a4a;
  --grey-body:#8a8a8a;
  --tile-grey:#6f6865;
  --white:#ffffff;
  --page:#ffffff;
}
*{box-sizing:border-box;margin:0;padding:0}
html,body{width:1200px;height:1123px;overflow:hidden;background:var(--page)}
body{position:relative;font-family:'Montserrat',Arial,sans-serif;color:var(--ink)}
.slide{position:absolute;width:387px;height:219px;overflow:hidden;background:var(--white);box-shadow:0 0 0 1px #e3e7ec}
.photo{position:absolute}
.photo.office{background:linear-gradient(135deg,#a9c4e3,#6f98c9 60%,#587fb3)}
.photo.team{background:linear-gradient(160deg,#c8d3df,#8ea3bb 55%,#4f5f72)}
.photo.paper{background:linear-gradient(135deg,#f1f3f6,#d9dfe7 60%,#c3ccd6)}
.photo.sky{background:linear-gradient(180deg,#9fb0c4,#6d7f95 60%,#2f3a47)}
.photo.shirt{background:linear-gradient(180deg,#f6f6f6 0%,#e9c9b6 30%,#c4363a 50%,#5b7397 85%)}
.footer{position:absolute;left:0;right:0;bottom:0;height:9px;background:var(--blue);color:var(--white);font-size:3.6px;line-height:9px;padding-left:4px}
.footer .num{position:absolute;right:0;top:0;width:18px;height:9px;background:var(--blue-soft);text-align:center;color:var(--white)}
.brand{position:absolute;display:flex;align-items:center;gap:3px;font-family:'Raleway',Arial,sans-serif;font-weight:700;color:var(--blue);letter-spacing:.3px}
.brand .dot{border-radius:50%;background:currentColor;flex:none}
.brand.small{font-size:10px}
.brand.small .dot{width:8px;height:8px}
.brand.stack{flex-direction:column;gap:2px}
.slide-title{position:absolute;left:17px;top:14px;font-family:'Raleway',Arial,sans-serif;font-size:17px;font-weight:400;color:var(--blue)}
.slide-title::after{content:"";position:absolute;left:0;bottom:-2px;width:20px;height:1px;background:var(--blue)}
.body{font-size:4.6px;line-height:1.45;color:var(--grey-body)}
.head-blue{color:var(--blue);font-weight:600}
.abs{position:absolute}
.white{color:var(--white)}
.icon-box{width:10px;height:10px;background:var(--blue);display:flex;align-items:center;justify-content:center;flex:none}
.icon-circle{width:14px;height:14px;border-radius:50%;background:var(--blue);display:flex;align-items:center;justify-content:center;flex:none}
.row{display:flex;gap:6px;align-items:flex-start}
.quote{font-family:'Raleway',Arial,sans-serif}
</style>
</head>
<body>

<!-- 1 cover -->
<section class="slide cover" style="left:6px;top:3px;background:linear-gradient(135deg,#7ea7d7,#4f85c4)">
  <div class="photo office" role="img" aria-label="Faded office desk scene under blue tint" style="inset:0;opacity:.45"></div>
  <div class="brand white" style="left:110px;top:92px;font-size:34px;gap:8px"><span class="dot" style="width:22px;height:22px"></span>VERNAPLO</div>
</section>

<!-- 2 title slide -->
<section class="slide title-photo" style="left:406px;top:3px">
  <div class="brand small" style="left:17px;top:6px"><span class="dot"></span>VERNAPLO</div>
  <div class="photo team" role="img" aria-label="Three engineers in hard hats reviewing plans" style="left:0;top:30px;width:387px;height:103px"></div>
  <div class="abs" style="left:0;top:132px;width:387px;height:42px;background:var(--blue-deep);text-align:center;color:var(--white)">
    <div class="quote" style="font-size:19px;margin-top:5px">Your Title Goes Here</div>
    <div style="font-size:6px">Your Subtitle Goes Here</div>
  </div>
  <div class="abs body" style="left:14px;top:180px;display:flex;gap:10px;font-size:4px">
    <div><div>Presented by</div><div class="head-blue" style="font-size:9px">&#9679; John Smith</div><div>VP Marketing</div></div>
    <div style="padding-top:5px"><div class="head-blue" style="font-size:9px">&#9679; Jane Smith</div><div>Senior Consultant</div></div>
    <div style="border-left:1px solid #ccc;padding-left:20px"><div>Presented for</div><div class="head-blue" style="font-size:9px">&#9679; Jack Brown</div><div>Vice President</div></div>
  </div>
  <div class="footer">&copy; 2016 VERNAPLO. All rights reserved<span class="num" style="width:40px;background:var(--blue-pale);color:var(--blue)">January 26, 2017</span></div>
</section>

<!-- 3 title slide light -->
<section class="slide title-light" style="left:806px;top:3px">
  <div class="photo paper" role="img" aria-label="Hand signing a document with a pen" style="left:0;top:0;width:387px;height:120px;opacity:.85"></div>
  <div class="abs" style="left:0;top:60px;width:387px;height:120px;background:linear-gradient(180deg,rgba(255,255,255,0),#fff 40%)"></div>
  <div class="brand stack" style="right:14px;top:8px;font-size:17px"><span class="dot" style="width:16px;height:16px"></span>VERNAPLO</div>
  <div class="abs quote" style="left:0;width:387px;top:146px;text-align:center;color:var(--blue);font-size:18px">Your Title Goes Here</div>
  <div class="abs" style="left:0;width:387px;top:163px;text-align:center;color:var(--blue-soft);font-size:6px">Your Subtitle Goes Here</div>
  <div class="abs" style="left:0;top:180px;width:387px;height:6px;background:var(--blue-pale)"></div>
  <div class="abs body" style="left:6px;top:203px;display:flex;gap:14px;font-size:4px;align-items:center">
    <span>Presented by</span><span class="head-blue" style="font-size:5.5px">&#9679; John Smith</span><span class="head-blue" style="font-size:5.5px">&#9679; Jane Smith</span><span>Presented for</span><span class="head-blue" style="font-size:5.5px">&#9679; Jack Brown</span><span style="font-size:5.5px;margin-left:20px">Cityname | January 26, 2017</span>
  </div>
  <div class="abs" style="left:0;right:0;bottom:0;height:3px;background:var(--blue)"></div>
</section>

<!-- 4 quote full -->
<section class="slide quote-full" style="left:6px;top:228px">
  <div class="photo team" role="img" aria-label="Engineers in hard hats studying a plan, blue tinted" style="inset:0"></div>
  <div class="abs" style="inset:0;background:rgba(60,120,195,.78)"></div>
  <div class="abs" style="left:177px;top:50px;width:32px;height:32px;border-radius:50%;background:var(--blue-deep);color:#fff;font-size:28px;text-align:center;line-height:42px;font-family:Georgia,serif">&ldquo;</div>
  <div class="abs quote white" style="left:0;width:387px;top:88px;text-align:center;font-size:12px;line-height:1.3">Coming together is a beginning.<br>Keeping together is progress.<br>Working together is success.</div>
  <div class="abs white" style="left:0;width:387px;top:142px;text-align:center;font-size:5.5px">- Marcel Dufresne -</div>
</section>

<!-- 5 agenda -->
<section class="slide agenda" style="left:406px;top:228px">
  <h2 class="slide-title">Our Agenda</h2>
  <div class="brand stack small" style="right:12px;top:10px"><span class="dot"></span>VERNAPLO</div>
  <div class="abs" style="left:52px;top:58px;display:grid;grid-template-columns:160px 160px;row-gap:18px">
    <div class="row"><div class="icon-box"><svg width="6" height="6" viewBox="0 0 6 6"><circle cx="3" cy="3" r="2.4" fill="none" stroke="#fff" stroke-width=".8"/><path d="M3 1.6V3h1.1" stroke="#fff" stroke-width=".6" fill="none"/></svg></div><div class="body"><div style="color:var(--ink);font-size:7px">Agenda One</div>10:00<br>Lorem ipsum dolor sit amet, consectetur<br>adipiscing elit, sed do eiusmod tempor labore</div></div>
    <div class="row"><div class="icon-box"><svg width="6" height="6" viewBox="0 0 6 6"><circle cx="3" cy="3" r="2.4" fill="none" stroke="#fff" stroke-width=".8"/><path d="M3 1.6V3h1.1" stroke="#fff" stroke-width=".6" fill="none"/></svg></div><div class="body"><div style="color:var(--ink);font-size:7px">Agenda Four</div>13:00<br>Lorem ipsum dolor sit amet, consectetur<br>adipiscing elit, sed do eiusmod tempor labore</div></div>
    <div class="row"><div class="icon-box"><svg width="6" height="6" viewBox="0 0 6 6"><circle cx="3" cy="3" r="2.4" fill="none" stroke="#fff" stroke-width=".8"/><path d="M3 1.6V3h1.1" stroke="#fff" stroke-width=".6" fill="none"/></svg></div><div class="body"><div style="color:var(--ink);font-size:7px">Agenda Two</div>11:00<br>Lorem ipsum dolor sit amet, consectetur<br>adipiscing elit, sed do eiusmod tempor labore</div></div>
    <div class="row"><div class="icon-box"><svg width="6" height="6" viewBox="0 0 6 6"><circle cx="3" cy="3" r="2.4" fill="none" stroke="#fff" stroke-width=".8"/><path d="M3 1.6V3h1.1" stroke="#fff" stroke-width=".6" fill="none"/></svg></div><div class="body"><div style="color:var(--ink);font-size:7px">Agenda Five</div>14:00<br>Lorem ipsum dolor sit amet, consectetur<br>adipiscing elit, sed do eiusmod tempor labore</div></div>
    <div class="row"><div class="icon-box"><svg width="6" height="6" viewBox="0 0 6 6"><circle cx="3" cy="3" r="2.4" fill="none" stroke="#fff" stroke-width=".8"/><path d="M3 1.6V3h1.1" stroke="#fff" stroke-width=".6" fill="none"/></svg></div><div class="body"><div style="color:var(--ink);font-size:7px">Agenda Three</div>12:00<br>Lorem ipsum dolor sit amet, consectetur<br>adipiscing elit, sed do eiusmod tempor labore</div></div>
    <div class="row"><div class="icon-box"><svg width="6" height="6" viewBox="0 0 6 6"><circle cx="3" cy="3" r="2.4" fill="none" stroke="#fff" stroke-width=".8"/><path d="M3 1.6V3h1.1" stroke="#fff" stroke-width=".6" fill="none"/></svg></div><div class="body"><div style="color:var(--ink);font-size:7px">Agenda Six</div>15:00<br>Lorem ipsum dolor sit amet, consectetur<br>adipiscing elit, sed do eiusmod tempor labore</div></div>
  </div>
  <div class="footer">&copy; 2017 VERNAPLO. All rights reserved.<span class="num">5</span></div>
</section>

<!-- 6 about -->
<section class="slide about" style="left:806px;top:228px">
  <div class="photo team" role="img" aria-label="Engineers in hard hats holding an unrolled plan" style="left:0;top:0;width:270px;height:210px"></div>
  <div class="brand stack small" style="right:12px;top:10px"><span class="dot"></span>VERNAPLO</div>
  <div class="abs white" style="left:193px;top:46px;width:194px;height:124px;background:rgba(58,120,196,.85);padding:14px 12px">
    <div class="quote" style="font-size:15px">About Us</div>
    <div style="width:22px;height:1px;background:#fff;margin:2px 0 5px"></div>
    <div style="font-size:4.6px;line-height:1.45">Lorem ipsum dolor sit amet, consectetur adipiscing elit, sed do eiusmod tempor incididunt ut labore et dolore magna aliqua.<br><br>Ut enim ad minim veniam, quis nostrud exercitation ullamco laboris nisi ut aliquip ex ea commodo consequat.</div>
  </div>
  <div class="footer">&copy; 2017 VERNAPLO. All rights reserved.<span class="num">6</span></div>
</section>

<!-- 7 services -->
<section class="slide services" style="left:6px;top:453px">
  <h2 class="slide-title">Our Services</h2>
  <div class="brand stack small" style="right:12px;top:10px"><span class="dot"></span>VERNAPLO</div>
  <div class="photo paper" role="img" aria-label="Hands reviewing printed charts on a desk" style="left:35px;top:50px;width:150px;height:95px"></div>
  <div class="abs body" style="left:35px;top:150px;width:150px"><div class="head-blue" style="font-size:6px">Your Title Goes Here</div>Lorem ipsum dolor sit amet, consectetur adipiscing elit, sed do eiusmod tempor incididunt ut labore et dolore magna aliqua. Ut enim ad minim veniam, quis nostrud exercitation ullamco laboris nisi ut aliquip ex ea commodo consequat.</div>
  <div class="abs" style="left:210px;top:52px;display:flex;flex-direction:column;gap:16px">
    <div class="row"><div class="icon-circle"><svg width="7" height="7" viewBox="0 0 7 7"><rect x="1" y="4" width="1.2" height="2.5" fill="#fff"/><rect x="3" y="2.5" width="1.2" height="4" fill="#fff"/><rect x="5" y="1" width="1.2" height="5.5" fill="#fff"/></svg></div><div class="body" style="width:130px"><div class="head-blue" style="font-size:7px;font-weight:500">Service Number One</div>Lorem ipsum dolor sit amet, consectetur adipiscing elit, sed do eiusmod tempor incididunt ut labore et dolore magna aliqua</div></div>
    <div class="row"><div class="icon-circle"><svg width="7" height="7" viewBox="0 0 7 7"><path d="M6 1L3 3.5 1 3l1.5 1.5L2 6.5l2-1 1.5 1.5-.5-2L6 1z" fill="#fff"/></svg></div><div class="body" style="width:130px"><div class="head-blue" style="font-size:7px;font-weight:500">Service Number Two</div>Lorem ipsum dolor sit amet, consectetur adipiscing elit, sed do eiusmod tempor incididunt ut labore et dolore magna aliqua</div></div>
    <div class="row"><div class="icon-circle"><svg width="7" height="7" viewBox="0 0 7 7"><circle cx="3" cy="3" r="2" fill="none" stroke="#fff" stroke-width="1"/><path d="M4.5 4.5L6.5 6.5" stroke="#fff" stroke-width="1"/></svg></div><div class="body" style="width:130px"><div class="head-blue" style="font-size:7px;font-weight:500">Service Number Three</div>Lorem ipsum dolor sit amet, consectetur adipiscing elit, sed do eiusmod tempor incididunt ut labore et dolore magna aliqua</div></div>
  </div>
  <div class="footer">&copy; 2017 VERNAPLO. All rights reserved.<span class="num">7</span></div>
</section>

<!-- 8 quote area -->
<section class="slide quote-area" style="left:406px;top:453px">
  <h2 class="slide-title">Quote Area</h2>
  <div class="brand stack small" style="right:12px;top:10px"><span class="dot"></span>VERNAPLO</div>
  <div class="abs" style="left:0;top:46px;width:192px;height:162px;background:linear-gradient(135deg,#5d8fc9,#3a72b8)"></div>
  <div class="photo sky" role="img" aria-label="Construction cranes silhouetted against a cloudy sky" style="left:192px;top:46px;width:195px;height:162px"></div>
  <div class="abs quote white" style="left:16px;top:80px;font-size:9.5px;line-height:1.3">&ldquo; Coming together is a<br>beginning.<br>Keeping together is progress.<br>Working together is success.</div>
  <div class="abs white" style="left:30px;top:138px;font-size:5.5px">- Marcel Dufresne -</div>
  <div class="footer">&copy; 2017 VERNAPLO. All rights reserved.<span class="num">8</span></div>
</section>

<!-- 9 text area -->
<section class="slide text-area" style="left:806px;top:453px">
  <h2 class="slide-title">Text Area</h2>
  <div class="brand stack small" style="right:12px;top:10px"><span class="dot"></span>VERNAPLO</div>
  <div class="abs head-blue" style="left:32px;top:68px;width:330px;font-size:8.5px;font-weight:700;line-height:1.3">This is place for your header text. Insert your text here, just replace this text with your own text</div>
  <div class="abs body" style="left:32px;top:96px;width:330px;font-size:5.6px">Lorem ipsum dolor sit amet, consectetur adipiscing elit, sed do eiusmod tempor incididunt ut labore et dolore magna aliqua. Ut enim ad minim veniam, quis nostrud exercitation ullamco laboris nisi ut aliquip ex ea commodo consequat.<br><br>Duis aute irure dolor in reprehenderit in voluptate velit esse cillum dolore eu fugiat nulla pariatur. Excepteur sint occaecat cupidatat non proident, sunt in culpa qui officia deserunt mollit anim id est laborum.<br><br>Ut enim ad minim veniam, quis nostrud exercitation ullamco laboris nisi ut aliquip ex ea commodo consequat.</div>
  <div class="footer">&copy; 2017 VERNAPLO. All rights reserved.<span class="num">9</span></div>
</section>

<!-- 10 vision -->
<section class="slide vision" style="left:6px;top:677px">
  <h2 class="slide-title">Our Vision &amp; Mission</h2>
  <div class="brand stack small" style="right:12px;top:10px"><span class="dot"></span>VERNAPLO</div>
  <div class="photo office" role="img" aria-label="Blue tinted desk with reports and charts" style="left:0;top:46px;width:387px;height:158px"></div>
  <div class="abs white" style="left:18px;top:70px;width:165px">
    <div class="quote" style="font-size:10px">&bull; Our Vision:</div>
    <div style="font-size:7.5px;font-weight:700;margin:3px 0 0 6px;line-height:1.3">Go to the Next Level<br>Without look in the past</div>
    <div style="width:38px;height:1px;background:#fff;margin:5px 0 5px 6px"></div>
    <div style="font-size:4.6px;line-height:1.45;margin-left:6px">Lorem ipsum dolor sit amet, consectetur adipiscing elit, sed do eiusmod tempor incididunt ut labore et dolore magna aliqua. Ut enim ad minim veniam, quis nostrud exercitation ullamco laboris nisi ut aliquip ex ea commodo consequat.</div>
  </div>
  <div class="abs white" style="left:222px;top:70px;width:150px">
    <div class="quote" style="font-size:10px">&bull; Our Missions:</div>
    <div style="display:flex;flex-direction:column;gap:7px;margin-top:5px">
      <div class="row"><div class="icon-circle" style="background:#fff"></div><div style="font-size:4.6px;line-height:1.4"><div style="font-size:6px">Your Text Here</div>Lorem ipsum dolor sit amet, consectetur adipiscing elit, sed do eiusmod tempor.</div></div>
      <div class="row"><div class="icon-circle" style="background:#fff"></div><div style="font-size:4.6px;line-height:1.4"><div style="font-size:6px">Your Text Here</div>Lorem ipsum dolor sit amet, consectetur adipiscing elit, sed do eiusmod tempor.</div></div>
      <div class="row"><div class="icon-circle" style="background:#fff"></div><div style="font-size:4.6px;line-height:1.4"><div style="font-size:6px">Your Text Here</div>Lorem ipsum dolor sit amet, consectetur adipiscing elit, sed do eiusmod tempor.</div></div>
    </div>
  </div>
  <div class="footer">&copy; 2017 VERNAPLO. All rights reserved.<span class="num">10</span></div>
</section>

<!-- 11 split -->
<section class="slide split" style="left:406px;top:677px">
  <div class="photo team" role="img" aria-label="Team of colleagues looking down at documents" style="left:0;top:0;width:193px;height:210px"></div>
  <div class="abs" style="left:0;top:72px;width:193px;height:70px;background:rgba(43,108,180,.8)"></div>
  <div class="brand white" style="left:40px;top:95px;font-size:18px;gap:5px"><span class="dot" style="width:13px;height:13px"></span>VERNAPLO</div>
  <div class="brand stack small" style="right:12px;top:10px"><span class="dot"></span>VERNAPLO</div>
  <div class="abs quote" style="left:212px;top:52px;font-size:17px;color:var(--blue);line-height:1.1">Your Title Goes<br>Here</div>
  <div class="abs" style="left:212px;top:94px;width:22px;height:1px;background:var(--blue)"></div>
  <div class="abs" style="left:212px;top:100px;display:flex;flex-direction:column;gap:10px">
    <div class="row"><div style="width:11px;height:11px;border-radius:50%;background:var(--blue);color:#fff;font-size:5px;text-align:center;line-height:11px">1</div><div class="body" style="width:120px"><div class="head-blue" style="font-size:6px;font-weight:500">Your Text Goes Here</div>Lorem ipsum dolor sit amet, consectetur adipiscing elit, sed do eiusmod tempor incididunt ut labore et dolore magna aliqua.</div></div>
    <div class="row"><div style="width:11px;height:11px;border-radius:50%;background:var(--blue);color:#fff;font-size:5px;text-align:center;line-height:11px">2</div><div class="body" style="width:120px"><div class="head-blue" style="font-size:6px;font-weight:500">Your Text Goes Here</div>Lorem ipsum dolor sit amet, consectetur adipiscing elit, sed do eiusmod tempor incididunt ut labore et dolore magna aliqua.</div></div>
  </div>
  <div class="footer">&copy; 2017 VERNAPLO. All rights reserved.<span class="num">11</span></div>
</section>

<!-- 12 tiles -->
<section class="slide tiles" style="left:806px;top:677px">
  <h2 class="slide-title">Your Title Goes Here</h2>
  <div class="brand stack small" style="right:12px;top:10px"><span class="dot"></span>VERNAPLO</div>
  <div class="photo team" role="img" aria-label="Engineers in hard hats around a table" style="left:28px;top:57px;width:107px;height:63px"></div>
  <div class="abs white" style="left:140px;top:57px;width:107px;height:63px;background:var(--blue-soft);padding:12px 8px;font-size:4.4px;line-height:1.4"><div style="font-size:6px;margin-bottom:3px">Heading Goes Here</div>Lorem ipsum dolor sit amet, consectetur adipiscing elit, sed do eiusmod tempor incididunt ut labore et dolore magna aliqua.</div>
  <div class="photo team" role="img" aria-label="Engineers in hard hats discussing plans" style="left:252px;top:57px;width:107px;height:63px"></div>
  <div class="abs white" style="left:28px;top:125px;width:107px;height:63px;background:var(--blue);padding:12px 8px;font-size:4.4px;line-height:1.4"><div style="font-size:6px;margin-bottom:3px">Heading Goes Here</div>Lorem ipsum dolor sit amet, consectetur adipiscing elit, sed do eiusmod tempor incididunt ut labore et dolore magna aliqua.</div>
  <div class="photo paper" role="img" aria-label="Hands pointing at printed charts" style="left:140px;top:125px;width:107px;height:63px"></div>
  <div class="abs white" style="left:252px;top:125px;width:107px;height:63px;background:var(--tile-grey);padding:12px 8px;font-size:4.4px;line-height:1.4"><div style="font-size:6px;margin-bottom:3px">Heading Goes Here</div>Lorem ipsum dolor sit amet, consectetur adipiscing elit, sed do eiusmod tempor incididunt ut labore et dolore magna aliqua.</div>
  <div class="footer">&copy; 2017 VERNAPLO. All rights reserved.<span class="num">12</span></div>
</section>

<!-- 13 blue panel -->
<section class="slide panel" style="left:6px;top:901px">
  <div class="photo team" role="img" aria-label="Engineers in hard hats reviewing a plan in an office" style="left:0;top:0;width:193px;height:210px"></div>
  <div class="abs" style="left:193px;top:0;width:194px;height:210px;background:var(--blue)"></div>
  <div class="brand stack white" style="right:14px;top:10px;font-size:10px"><span class="dot" style="width:8px;height:8px"></span>VERNAPLO</div>
  <div class="abs white" style="left:212px;top:58px;display:flex;flex-direction:column;gap:13px">
    <div class="row"><svg width="10" height="10" viewBox="0 0 10 10"><circle cx="4" cy="4" r="3" fill="none" stroke="#fff" stroke-width="1.4"/><path d="M6.2 6.2L9 9" stroke="#fff" stroke-width="1.6"/></svg><div style="font-size:4.6px;line-height:1.4"><div style="font-size:6.5px">Your Text Here</div>Lorem ipsum dolor sit amet, consectetur<br>adipiscing elit, sed do eiusmod.</div></div>
    <div class="row"><svg width="10" height="10" viewBox="0 0 10 10"><path d="M1 9l1-3 5-5 2 2-5 5z" fill="#fff"/></svg><div style="font-size:4.6px;line-height:1.4"><div style="font-size:6.5px">Your Text Here</div>Lorem ipsum dolor sit amet, consectetur<br>adipiscing elit, sed do eiusmod.</div></div>
    <div class="row"><svg width="10" height="10" viewBox="0 0 10 10"><path d="M9 1L4 5 1 4l2 2-1 3 3-1 2 2 0-3z" fill="#fff"/></svg><div style="font-size:4.6px;line-height:1.4"><div style="font-size:6.5px">Your Text Here</div>Lorem ipsum dolor sit amet, consectetur<br>adipiscing elit, sed do eiusmod.</div></div>
    <div class="row"><svg width="10" height="10" viewBox="0 0 10 10"><circle cx="5" cy="5" r="3.2" fill="none" stroke="#fff" stroke-width="2" stroke-dasharray="1.6 1"/><circle cx="5" cy="5" r="1.2" fill="#fff"/></svg><div style="font-size:4.6px;line-height:1.4"><div style="font-size:6.5px">Your Text Here</div>Lorem ipsum dolor sit amet, consectetur<br>adipiscing elit, sed do eiusmod.</div></div>
  </div>
  <div class="footer">&copy; 2017 VERNAPLO. All rights reserved.<span class="num">13</span></div>
</section>

<!-- 14 feature -->
<section class="slide feature" style="left:406px;top:901px">
  <div class="abs" style="left:10px;top:5px;width:122px;height:95px;background:linear-gradient(135deg,#7ea7d7,#4f85c4)"></div>
  <div class="brand white" style="left:22px;top:46px;font-size:14px;gap:4px"><span class="dot" style="width:10px;height:10px"></span>VERNAPLO</div>
  <div class="photo paper" role="img" aria-label="Hands working on documents at a desk" style="left:10px;top:105px;width:122px;height:95px"></div>
  <div class="photo shirt" role="img" aria-label="Smiling worker in a hard hat giving a thumbs up" style="left:140px;top:5px;width:110px;height:200px"></div>
  <div class="brand stack small" style="right:12px;top:10px"><span class="dot"></span>VERNAPLO</div>
  <div class="abs quote" style="left:262px;top:34px;font-size:16px;color:var(--blue);line-height:1.05">Your Title<br>Goes Here</div>
  <div class="abs body" style="left:262px;top:80px;width:112px;font-size:4.6px">Lorem ipsum dolor sit amet, consectetur adipiscing elit, sed do eiusmod tempor incididunt ut labore et dolore magna aliqua.<br><br>Duis aute irure dolor in reprehenderit in voluptate velit esse cillum dolore eu fugiat nulla pariatur.<br><br>Ut enim ad minim veniam, quis nostrud exercitation ullamco laboris nisi ut aliquip ex ea commodo consequat.</div>
  <div class="footer">&copy; 2017 VERNAPLO. All rights reserved.<span class="num">14</span></div>
</section>

<!-- 15 text with images -->
<section class="slide text-images" style="left:806px;top:901px">
  <h2 class="slide-title">Your Title Goes Here</h2>
  <div class="brand stack small" style="right:12px;top:10px"><span class="dot"></span>VERNAPLO</div>
  <div class="abs head-blue" style="left:32px;top:66px;width:150px;font-size:8px;font-weight:700;line-height:1.3">This is place for your header text. Insert your text here</div>
  <div class="abs body" style="left:32px;top:90px;width:150px;font-size:5.2px">Lorem ipsum dolor sit amet, consectetur adipiscing elit, sed do eiusmod tempor incididunt ut labore et dolore magna aliqua. Ut enim ad minim veniam, quis nostrud exercitation.<br><br>Excepteur sint occaecat cupidatat non proident, sunt in culpa qui officia deserunt mollit anim id est laborum.</div>
  <div class="photo paper" role="img" aria-label="Hands holding a pen over paperwork" style="left:194px;top:60px;width:56px;height:125px"></div>
  <div class="photo paper" role="img" aria-label="Close-up of a contract document" style="left:258px;top:60px;width:56px;height:125px;background:linear-gradient(160deg,#e8edf3,#b9cbe0)"></div>
  <div class="photo paper" role="img" aria-label="Hands using a tablet on a desk" style="left:322px;top:60px;width:56px;height:125px"></div>
  <div class="footer">&copy; 2017 VERNAPLO. All rights reserved.<span class="num">15</span></div>
</section>

</body>
</html>
```